Design and Renovation Company Luxury Business Card

I want to create a luxury business card for a Design and Renovation Firm . We will use our current logo. The company name is 742BUILD. We do not want anything standard. We need a very unique concept.
Please see uploaded inspiration. I really like the textured paper option. I would like the card to be thick with debossing, and/or embossing options. The logo has orange in it but I would like to see the card with and without the orange. I think the orange may make the company feel less high-end. The goal is to elevate the logo not match its vibe per se of the logo. We want something very unique, not standard at all!
I would like a space for :
Logo,
Name,
Position,
Email,
Office number,
Website Address,
Business Address,
Thank you!
Have fun!
Target Market(s)
Home owners Age 35 +
Industry/Entity Type
Design and Renovation
Contact Information for Business Card
Logo, Name, Position, Email, Office number, Website Address, Business Address,.
Colors
Designer to choose colors to be used in the design.
Requirements
Must have
- A luxury designer feel. Must be black or dark grey but open to other luxury ideas.
Nice to have
- Gold, silver, black embossing or debossing. Textured paper design.
Should not have
- A cheap look and feel.

```html
<!DOCTYPE html>
<html lang="en">
<head>
<meta charset="utf-8">
<title>742BUILD Business Card</title>
<link rel="stylesheet" href="https://fonts.googleapis.com/css2?family=Montserrat:wght@500;600&display=swap">
<style>
  :root {
    --backdrop: #e2e0e2;
    --card: #161616;
    --gold: #e2c12f;
  }
  * { margin: 0; padding: 0; box-sizing: border-box; }
  html, body { width: 1200px; height: 1200px; overflow: hidden; }
  body { background: var(--backdrop); position: relative; font-family: "Montserrat", sans-serif; }

  .card {
    position: absolute;
    left: 182px;
    width: 854px;
    background: var(--card);
    color: var(--gold);
  }
  .card--front {
    top: 90px;
    height: 486px;
    display: flex;
    align-items: center;
    justify-content: center;
  }
  .card--back { top: 626px; height: 488px; }

  /* Front: centred name and tagline */
  .brand { display: flex; flex-direction: column; align-items: center; }
  .brand__name {
    font-weight: 600;
    font-size: 52px;
    line-height: 56px;
    letter-spacing: 1px;
  }
  .brand__tagline {
    font-weight: 600;
    font-size: 13px;
    letter-spacing: 2px;
    margin-top: 4px;
  }

  /* Back: person, company name, contact */
  .person { position: absolute; left: 58px; top: 62px; }
  .person__name {
    font-weight: 600;
    font-size: 29px;
    letter-spacing: 0.5px;
    line-height: 34px;
  }
  .person__role {
    font-weight: 500;
    font-size: 25px;
    line-height: 30px;
  }

  .company {
    position: absolute;
    right: 68px;
    top: 164px;
    font-weight: 600;
    font-size: 22px;
    line-height: 26px;
  }

  .contact {
    position: absolute;
    left: 58px;
    top: 309px;
    list-style: none;
  }
  .contact__item {
    display: flex;
    align-items: center;
    gap: 14px;
    height: 30px;
    font-weight: 500;
    font-size: 17px;
    letter-spacing: 3px;
  }
  .contact__icon { width: 22px; height: 22px; flex: none; }
</style>
</head>
<body>

  <section class="card card--front" aria-label="Card front">
    <div class="brand">
      <span class="brand__name">742BUILD</span>
      <span class="brand__tagline">Design and Renovation Firm</span>
    </div>
  </section>

  <section class="card card--back" aria-label="Card back">
    <div class="person">
      <p class="person__name">MARCUS ELLERY</p>
      <p class="person__role">Founder</p>
    </div>

    <span class="company">742BUILD</span>

    <ul class="contact">
      <li class="contact__item">
        <svg class="contact__icon" viewBox="0 0 22 22" aria-hidden="true">
          <rect width="22" height="22" fill="var(--gold)"/>
          <path d="M11 4a5 5 0 0 0-5 5c0 4 5 9 5 9s5-5 5-9a5 5 0 0 0-5-5z" fill="var(--card)"/>
          <circle cx="11" cy="9" r="2" fill="var(--gold)"/>
        </svg>
        <span>Anywhere St.Any City, ST 12345</span>
      </li>
      <li class="contact__item">
        <svg class="contact__icon" viewBox="0 0 22 22" aria-hidden="true">
          <rect width="22" height="22" fill="var(--gold)"/>
          <path d="M7 4h3l1 4-2 1.5c.8 1.8 2 3 3.5 3.5L14 11l4 1v3c0 1-1 2-2 2C10 17 5 12 5 6c0-1 1-2 2-2z" fill="var(--card)"/>
        </svg>
        <span>07700 900 418</span>
      </li>
      <li class="contact__item">
        <svg class="contact__icon" viewBox="0 0 22 22" aria-hidden="true">
          <rect width="22" height="22" fill="var(--gold)"/>
          <rect x="4" y="6" width="14" height="10" fill="var(--card)"/>
          <path d="M4 6l7 6 7-6" fill="none" stroke="var(--gold)" stroke-width="1.4"/>
        </svg>
        <span>studio@742build.com</span>
      </li>
      <li class="contact__item">
        <svg class="contact__icon" viewBox="0 0 22 22" aria-hidden="true">
          <rect width="22" height="22" fill="var(--gold)"/>
          <circle cx="11" cy="11" r="6.5" fill="var(--card)"/>
          <path d="M4.5 11h13M11 4.5c-2.5 3-2.5 10 0 13M11 4.5c2.5 3 2.5 10 0 13" fill="none" stroke="var(--gold)" stroke-width="1.1"/>
        </svg>
        <span>www.yoursite.com</span>
      </li>
    </ul>
  </section>

</body>
</html>
```